Dog grooming business card
This is a business card for m dog grooming business like it say above.
In the priorities box below I will have the text that I want on the card.

Industry/Entity Type

Business

Colors

Designer to choose colors to be used in the design.

Requirements
Must have
• My logo and the insurance stamp must be on the card.

Text it must have :

Professional grooming services
Email: lunabrisk@mailvane.net
Text or call 1 705 318 6642
TKV certified/member
Pet first aid certified
Next appointment ___________________________________
Nice to have
• Greens to match my logo

```html
<!DOCTYPE html>
<html lang="en">
<head>
<meta charset="utf-8">
<title>Luna Brisk – Business Card</title>
<link rel="stylesheet" href="https://fonts.googleapis.com/css2?family=Open+Sans:wght@400;600;700&family=Old+Standard+TT:wght@700&display=swap">
<style>
  :root {
    --bg: #2a2a2c;
    --green: #9bc53d;
    --green-text: #8cb83a;
    --white: #ffffff;
    --ink: #1d1d1d;
    --grey-text: #3a3a3a;
    --badge-blue: #3f7fc4;
  }
  * { margin: 0; padding: 0; box-sizing: border-box; }
  html, body { width: 1200px; height: 800px; overflow: hidden; }
  body {
    background: var(--bg);
    font-family: "Open Sans", Arial, sans-serif;
    position: relative;
  }
  .card {
    position: absolute;
    width: 520px;
    height: 297px;
    border-radius: 6px;
    overflow: hidden;
    box-shadow: 0 10px 30px rgba(0,0,0,.45);
  }
  .card-front { left: 50px; top: 252px; background: var(--green); }
  .card-back { left: 630px; top: 252px; background: var(--green); }
  .card-art { position: absolute; inset: 0; }

  .brand {
    position: absolute;
    display: flex;
    align-items: center;
    gap: 10px;
    color: var(--green-text);
    font-weight: 700;
    white-space: nowrap;
  }
  .brand-mark {
    border-radius: 50%;
    background: var(--green);
    flex: none;
  }
  .card-front .brand { left: 120px; top: 126px; font-size: 34px; }
  .card-front .brand-mark { width: 36px; height: 36px; }
  .card-back .brand { left: 285px; top: 40px; font-size: 26px; }
  .card-back .brand-mark { width: 28px; height: 28px; }

  .tagline {
    position: absolute;
    left: 262px; top: 88px;
    font-family: "Old Standard TT", Georgia, serif;
    font-weight: 700;
    font-size: 17px;
    color: var(--grey-text);
  }
  .holder {
    position: absolute;
    left: 44px; top: 58px;
  }
  .holder-name { color: var(--green-text); font-weight: 600; font-size: 19px; line-height: 1.1; }
  .holder-role { color: var(--grey-text); font-size: 13px; }
  .contact {
    position: absolute;
    right: 26px; top: 122px;
    text-align: right;
    list-style: none;
    color: var(--green-text);
    font-size: 13px;
    line-height: 1.55;
  }
  .contact .gap { margin-top: 8px; }
  .appointment {
    position: absolute;
    right: 26px; top: 222px;
    font-size: 12px;
    color: var(--grey-text);
    white-space: nowrap;
  }
  .insurance-stamp {
    position: absolute;
    left: 12px; bottom: 12px;
    width: 140px; height: 62px;
    background: var(--white);
    border: 3px solid var(--badge-blue);
    border-radius: 12px;
  }
</style>
</head>
<body>
  <section class="card card-front" aria-label="Card front">
    <svg class="card-art" viewBox="0 0 520 297" aria-hidden="true">
      <ellipse cx="245" cy="140" rx="205" ry="120" transform="rotate(-12 245 140)" fill="var(--white)" stroke="var(--ink)" stroke-width="7"/>
    </svg>
    <div class="brand"><span class="brand-mark"></span>Luna Brisk</div>
  </section>

  <section class="card card-back" aria-label="Card back">
    <svg class="card-art" viewBox="0 0 520 297" aria-hidden="true">
      <path d="M0 0 H520 V262 C200 255 30 200 0 110 Z" fill="var(--white)"/>
      <path d="M0 110 C30 200 200 255 520 262" fill="none" stroke="var(--ink)" stroke-width="6"/>
      <path d="M40 56 C30 71 30 91 40 104" fill="none" stroke="var(--ink)" stroke-width="2"/>
      <path d="M150 48 C165 58 168 76 160 88" fill="none" stroke="var(--ink)" stroke-width="2"/>
    </svg>
    <div class="holder">
      <p class="holder-name">Dara Quill</p>
      <p class="holder-role">Manager</p>
    </div>
    <div class="brand"><span class="brand-mark"></span>Luna Brisk</div>
    <p class="tagline">Professional grooming services</p>
    <ul class="contact">
      <li>Text or call 1 705 318 6642</li>
      <li class="gap">lunabrisk@mailvane.net</li>
      <li>Pet first aid certified</li>
      <li>TKV certified/member</li>
    </ul>
    <p class="appointment">Next appointment ______________________</p>
    <div class="insurance-stamp" role="img" aria-label="Insurance stamp"></div>
  </section>
</body>
</html>
```